Home Inspection Postcard Design

Home inspection. Attached is my old postcard. I would like the card to have the same verbage on it - front and back. but I would like the house graphic and the colors to be blues. The only changes to the information is the website address is www.brightoakhps.com. THe PO Box is now 381 rather than 647, and I wanted to add my email address which is brightoakhps@quillmail.net. I would like to keep the $25 off box but add "or a 10% military discount, which ever is greater" or something like that .If you could mock something up for me I would really appreciate it. I would also like a glossy finish on the cards

Home Inspection

```html
<!DOCTYPE html>
<html lang="en">
<head>
<meta charset="utf-8">
<title>Brightoak Home Inspection Services – Postcard</title>
<link rel="stylesheet" href="https://fonts.googleapis.com/css2?family=Roboto+Condensed:ital,wght@0,400;0,700;1,400&family=Playfair+Display:ital,wght@1,700&family=Arimo:wght@700&display=swap">
<style>
  :root {
    --brand-blue: #1f5fa8;
    --brand-blue-dark: #163f73;
    --brand-blue-light: #cfe4ff;
    --badge-edge: #2d3e55;
    --ink: #3c3c3c;
    --paper: #f4f6f9;
    --white: #ffffff;
  }
  * { box-sizing: border-box; margin: 0; padding: 0; }
  html, body { width: 788px; height: 1200px; overflow: hidden; }
  body { background: var(--white); position: relative; font-family: "Roboto Condensed", sans-serif; color: var(--ink); }

  .card { position: absolute; left: 26px; width: 736px; overflow: hidden; background: var(--paper); box-shadow: 0 2px 6px rgba(0,0,0,.25); }
  .card--front { top: 25px; height: 558px; background: linear-gradient(#f7f8fa, #eceef2); }
  .card--back { top: 604px; height: 571px; }

  /* Front */
  .couple-photo { position: absolute; left: 24px; top: 0; width: 490px; height: 380px;
    background: radial-gradient(ellipse at 45% 40%, #c9b7a6 0%, #8e9fb5 45%, #d9dee6 80%, #eff1f4 100%); }
  .front-band { position: absolute; left: 0; top: 0; width: 736px; height: 558px; }
  .brand-box { position: absolute; background: var(--white); border: 2px solid var(--brand-blue);
    display: flex; flex-direction: column; align-items: center; justify-content: center; text-align: center; }
  .card--front .brand-box { left: 510px; top: 21px; width: 200px; height: 198px; }
  .brand-mark { width: 34px; height: 34px; border-radius: 50%; background: var(--brand-blue); margin-bottom: 12px; }
  .brand-name { font-weight: 400; font-size: 15px; line-height: 1.2; color: var(--ink); white-space: nowrap; }
  .brand-phone { font-family: "Arimo", sans-serif; font-weight: 700; font-size: 24px; color: #111; margin-top: 10px; }

  .tagline { position: absolute; right: 30px; top: 232px; font-family: "Playfair Display", serif; font-style: italic; font-weight: 700; font-size: 18px; color: var(--ink); }
  .credentials { position: absolute; right: 32px; top: 264px; font-weight: 700; font-size: 16px; color: var(--brand-blue); letter-spacing: .2px; }

  .offer-badge { position: absolute; left: 24px; top: 350px; width: 170px; height: 186px; }
  .offer-text { position: absolute; left: 29px; top: 360px; width: 160px; text-align: center; color: var(--white); font-weight: 700; text-transform: uppercase; font-size: 15px; line-height: 1.3; }
  .offer-text .amount { font-size: 29px; color: var(--brand-blue-light); line-height: 1.1; }
  .offer-text .amount small { font-size: 19px; }
  .offer-text .military { margin: 6px auto 0; width: 132px; font-size: 12px; line-height: 1.25; text-transform: none; font-weight: 400; }
  .offer-text .military b { font-weight: 700; color: var(--brand-blue-light); }

  .pitch { position: absolute; left: 257px; top: 344px; width: 457px; }
  .pitch__title { text-align: right; font-family: "Playfair Display", serif; font-style: italic; font-weight: 700; font-size: 23px; color: var(--brand-blue); }
  .pitch__subtitle { text-align: right; font-family: "Playfair Display", serif; font-style: italic; font-size: 16px; color: var(--ink); margin-top: 2px; font-weight: 700; letter-spacing: -.2px; }
  .pitch__body { margin-top: 8px; font-size: 13.6px; line-height: 19.6px; color: var(--ink); text-align: justify; }

  /* Back */
  .inspection-photo { position: absolute; inset: 0;
    background: linear-gradient(160deg, #f1f2f4 0%, #dcdee2 35%, #bcc0c6 65%, #e4e6e9 100%); }
  .card--back .brand-box { left: 22px; top: 24px; width: 166px; height: 164px; }
  .card--back .brand-mark { width: 28px; height: 28px; margin-bottom: 10px; }
  .card--back .brand-name { font-size: 12.5px; }
  .card--back .brand-phone { font-size: 19px; margin-top: 8px; }

  .contact-list { position: absolute; left: 206px; top: 82px; list-style: none; }
  .contact-list li { display: flex; align-items: center; height: 31px; font-size: 17px; color: #333; }
  .contact-list svg { width: 16px; height: 16px; margin-right: 12px; flex: none; }

  .reasons { position: absolute; left: 30px; top: 212px; width: 310px; }
  .reasons__title { font-family: "Playfair Display", serif; font-style: italic; font-weight: 700; font-size: 23px; color: var(--brand-blue); }
  .reasons__list { margin-top: 14px; padding-left: 17px; font-size: 15px; line-height: 20.5px; color: #2f2f2f; }
  .reasons__list li { margin-bottom: 2px; padding-left: 2px; }
</style>
</head>
<body>

<section class="card card--front" aria-label="Postcard front">
  <div class="couple-photo" role="img" aria-label="Photo of a smiling couple holding up keys to their new home"></div>

  <svg class="front-band" viewBox="0 0 736 558" aria-hidden="true">
    <defs>
      <linearGradient id="band-fill" x1="0" y1="0" x2="0" y2="1">
        <stop offset="0" stop-color="#e9ecf1"/>
        <stop offset="1" stop-color="#c3c9d2"/>
      </linearGradient>
    </defs>
    <path d="M0 345 C 150 330, 260 390, 420 320 C 540 268, 640 300, 736 290 L736 558 L0 558 Z" fill="url(#band-fill)"/>
    <path d="M0 345 C 150 330, 260 390, 420 320 C 540 268, 640 300, 736 290" fill="none" stroke="#7f8896" stroke-width="2"/>
  </svg>

  <div class="brand-box">
    <span class="brand-mark" aria-hidden="true"></span>
    <span class="brand-name">Brightoak<br>Home Inspection Services LLC</span>
    <span class="brand-phone">912-555-0148</span>
  </div>

  <p class="tagline">“We leave no stone unturned”</p>
  <p class="credentials">LICENSED, CERTIFIED &amp; INSURED</p>

  <svg class="offer-badge" viewBox="0 0 170 186" aria-hidden="true">
    <polygon points="0,0 170,0 170,150 85,186 0,150" fill="var(--badge-edge)"/>
    <polygon points="5,0 165,0 165,147 85,180 5,147" fill="var(--brand-blue)"/>
    <polygon points="5,0 165,0 165,147 85,180 5,147" fill="none" stroke="var(--brand-blue-dark)" stroke-width="2" stroke-dasharray="7 5"/>
  </svg>
  <div class="offer-text">
    <div class="amount">$25 <small>OFF</small></div>
    <div>With this<br>postcard</div>
    <div class="military">or a <b>10% military discount</b>, whichever is greater</div>
  </div>

  <div class="pitch">
    <h1 class="pitch__title">Confidence in Home Buying</h1>
    <p class="pitch__subtitle">Enjoy peace of mind before buying your new home.</p>
    <p class="pitch__body">Our trained professionals inspect the property and immediately present you with a detailed, yet clear report. They will answer any questions you may have. Join our experienced inspectors in their tour of the property. They will acquaint you with its strengths and weaknesses. You will feel confident in their judgment and thoroughness. Many realtors, sellers, home buyers, mortgage companies, and relocation companies have used our services to their satisfaction.</p>
  </div>
</section>

<section class="card card--back" aria-label="Postcard back">
  <div class="inspection-photo" role="img" aria-label="Faded greyscale photo of a home inspections report with keys and a pen"></div>

  <div class="brand-box">
    <span class="brand-mark" aria-hidden="true"></span>
    <span class="brand-name">Brightoak<br>Home Inspection Services LLC</span>
    <span class="brand-phone">912-555-0148</span>
  </div>

  <ul class="contact-list">
    <li>
      <svg viewBox="0 0 16 16" aria-hidden="true"><path d="M8 1a5 5 0 0 0-5 5c0 3.8 5 9 5 9s5-5.2 5-9a5 5 0 0 0-5-5zm0 7a2 2 0 1 1 0-4 2 2 0 0 1 0 4z" fill="var(--brand-blue)"/></svg>
      PO Box 381, Marlow Creek, GA 31399
    </li>
    <li>
      <svg viewBox="0 0 16 16" aria-hidden="true"><circle cx="8" cy="8" r="6.5" fill="none" stroke="var(--brand-blue)" stroke-width="1.4"/><rect x="7.3" y="7" width="1.4" height="5" fill="var(--brand-blue)"/><circle cx="8" cy="4.8" r=".9" fill="var(--brand-blue)"/></svg>
      www.brightoakhps.com
    </li>
    <li>
      <svg viewBox="0 0 16 16" aria-hidden="true"><rect x="1.5" y="3.5" width="13" height="9" fill="none" stroke="var(--brand-blue)" stroke-width="1.4"/><path d="M1.5 3.5 8 9l6.5-5.5" fill="none" stroke="var(--brand-blue)" stroke-width="1.4"/></svg>
      brightoakhps@quillmail.net
    </li>
  </ul>

  <div class="reasons">
    <h2 class="reasons__title">Why do I need an inspection?</h2>
    <ul class="reasons__list">
      <li>Peace of mind – Puts the buyer’s mind at ease that the home is in good shape.</li>
      <li>Renegotiate – If problems do arise, the buyer can negotiate a lower price or ask the seller to make repairs.</li>
      <li>Opt-out – If the problems are too big or unsettling, the buyer can opt-out of buying the home.</li>
      <li>Future needs – Buyers can learn about potential maintenance and upkeep.</li>
    </ul>
  </div>
</section>

</body>
</html>
```